Tellwick Asset Management - Corporate Letter Head Project

Looking for a classy design based on our current logo. Please find current logo source file in files. With our color scheme.

Target Market(s)

We're an investment firm, the letterhead needs to look professional and attractive to clients.

Industry/Entity Type

Hedgefund

Colors
0054AA
0677BA
7BADD7
CADEEF
E8F1F8

Requirements
Must have
• Our logo, address, phone number, and email

```html
<!DOCTYPE html>
<html lang="en">
<head>
<meta charset="utf-8">
<title>Tellwick Asset Management – Letterhead</title>
<link rel="stylesheet" href="https://fonts.googleapis.com/css2?family=Montserrat:wght@400&display=swap">
<style>
  :root {
    --backdrop: #e9ecef;
    --navy: #0e2a4a;
    --paper: #ffffff;
    --ink-light: #ffffff;
    --divider: rgba(255,255,255,0.85);
  }
  html, body {
    margin: 0;
    padding: 0;
    width: 1200px;
    height: 1200px;
    overflow: hidden;
    background: var(--backdrop);
    font-family: "Montserrat", sans-serif;
  }
  .canvas {
    width: 1200px;
    height: 1200px;
    display: flex;
    align-items: center;
    justify-content: center;
  }
  .letterhead {
    width: 800px;
    height: 1090px;
    background: var(--paper);
    box-shadow: 0 6px 24px rgba(0,0,0,0.12);
    position: relative;
  }
  .letterhead-header {
    height: 150px;
    background: var(--navy);
    display: flex;
    align-items: center;
    padding: 0 44px 0 54px;
    box-sizing: border-box;
    color: var(--ink-light);
  }
  .brand {
    display: flex;
    align-items: center;
    gap: 18px;
    flex: 1;
  }
  .brand-square {
    width: 54px;
    height: 54px;
    border: 1.5px solid var(--ink-light);
    box-sizing: border-box;
  }
  .brand-name {
    font-size: 26px;
    font-weight: 400;
    letter-spacing: 0.04em;
    color: var(--ink-light);
    margin: 0;
  }
  .header-divider {
    width: 1px;
    height: 64px;
    background: var(--divider);
    margin: 0 36px 0 0;
    transform: rotate(14deg);
  }
  .contact {
    font-size: 13px;
    line-height: 1.45;
    font-style: normal;
  }
  .contact-address { margin-bottom: 6px; }
  .contact-line {
    display: flex;
    align-items: center;
    gap: 6px;
  }
  .contact-line svg { width: 11px; height: 11px; fill: var(--ink-light); }
</style>
</head>
<body>
<main class="canvas">
  <article class="letterhead">
    <header class="letterhead-header">
      <div class="brand">
        <span class="brand-square" aria-hidden="true"></span>
        <h1 class="brand-name">Tellwick Asset Management</h1>
      </div>
      <span class="header-divider" aria-hidden="true"></span>
      <address class="contact">
        <div class="contact-address">Your address, City<br>State, Zip 123400</div>
        <div class="contact-line">
          <svg viewBox="0 0 24 24" aria-hidden="true"><path d="M6.6 10.8a15.1 15.1 0 0 0 6.6 6.6l2.2-2.2a1 1 0 0 1 1-.25 11.4 11.4 0 0 0 3.6.57 1 1 0 0 1 1 1V20a1 1 0 0 1-1 1A17 17 0 0 1 3 4a1 1 0 0 1 1-1h3.5a1 1 0 0 1 1 1c0 1.25.2 2.45.57 3.57a1 1 0 0 1-.25 1z"/></svg>
          <span>123 456 789 000</span>
        </div>
        <div class="contact-line">
          <svg viewBox="0 0 24 24" aria-hidden="true"><path d="M2 5h20v14H2zm2 2v.5l8 5 8-5V7zm0 2.9V17h16V9.9l-8 5z"/></svg>
          <span>info@tellwickasset.com</span>
        </div>
      </address>
    </header>
  </article>
</main>
</body>
</html>
```